Law Firm Header Revision

Task: Redesign my law firm Word document header (modern, succinct, logo-first, easy address updates)

I need you to revise and modernize my Microsoft Word document header for Law Office of Corbin Alvey, PLLC. The result should look professional and clean on letters (including Letters of Protection), with the logo as the main focus and the text kept succinct.

Goals:
1. Create a modern, minimal header that feels premium and uncluttered.
Make the logo the most visually dominant element.
Reduce the visual weight of the contact/address block so it doesn’t distract from the document.
Make the address easy to change later (I’m moving offices soon) while keeping the same header design.

2. Content to include (keep all info accurate):
Law Office of Corbin Alvey, PLLC
615 Marlowe St. Ste #300-214, Houston, TX 77002
Office: 832.555.0143
Direct: 713.555.0186
Fax: 832.555.0127
Calveylegal.example

3. Layout requirements:
Provide 3 header style options:
Logo left + contact info right
Centered logo + single concise contact line below
Logo left + firm name prominent + minimal contact line
The primary line near the logo should be minimal (preferably website + main office phone).
The address should be easy to update in one place without redesigning the header. Prefer either:
Move the full address to the footer, or
Put the address in a single dedicated line/block so I can edit it once and keep the layout unchanged.
4. Build constraints:
Must be achievable using standard Microsoft Word tools only (header/footer, tables, alignment, fonts, spacing). No advanced graphics software.
Provide exact header text, plus step-by-step Word instructions for each option:
Font recommendations + sizes
Alignment
Spacing
Table setup (if used)
How to keep it consistent across pages

5. Deliverable:
For each of the 3 options, provide:
The exact header content (with line breaks)
Formatting specs (fonts, sizes, spacing)
Word build steps so I can recreate it reliably and keep the logo as the focal point.

```html
<!DOCTYPE html>
<html lang="en">
<head>
<meta charset="UTF-8">
<title>Corbin Alvey Law – Letterhead</title>
<link rel="stylesheet" href="https://fonts.googleapis.com/css2?family=Oranienbaum&family=Poppins:wght@400;600&display=swap">
<style>
  :root {
    --backdrop: #474747;
    --paper: #ffffff;
    --navy: #0f1d33;
    --ink: #4a4a4a;
    --link-blue: #2a5db0;
    --swoosh-grey: #c4c4c4;
    --rule-grey: #5a5a5a;
  }
  * { margin: 0; padding: 0; box-sizing: border-box; }
  html, body { width: 1200px; height: 1200px; overflow: hidden; background: var(--backdrop); }
  .letterhead {
    position: absolute; left: 220px; top: 63px; width: 759px; height: 1073px;
    background: var(--paper);
    box-shadow: 0 4px 10px rgba(0,0,0,0.45);
    font-family: "Poppins", sans-serif; color: var(--ink);
  }
  .header-swoosh { position: absolute; left: 0; top: 0; width: 759px; height: 240px; }
  .brand {
    position: absolute; top: 35px; left: 0; width: 100%;
    display: flex; justify-content: center; align-items: flex-start; gap: 15px;
  }
  .brand-square { width: 78px; height: 75px; background: var(--navy); flex: none; }
  .brand-name {
    font-family: "Oranienbaum", serif; color: var(--navy);
    display: flex; flex-direction: column; align-items: stretch; white-space: nowrap;
  }
  .brand-name .firm { font-size: 60px; line-height: 52px; letter-spacing: 0.5px; text-align: center; margin-top: 2px; }
  .brand-name .practice-row { display: flex; align-items: center; gap: 12px; margin-top: 4px; }
  .brand-name .practice-row .rule { flex: 1; height: 1.6px; background: var(--navy); }
  .brand-name .practice { font-size: 25px; line-height: 22px; letter-spacing: 11px; padding-left: 11px; }
  .website {
    position: absolute; top: 129px; left: 0; width: 100%; text-align: center;
    font-size: 14px; line-height: 20px; color: var(--link-blue); letter-spacing: 9px; padding-left: 9px;
  }
  .address-box {
    position: absolute; top: 152px; left: 43px; width: 674px; height: 25px;
    border: 1.3px solid var(--rule-grey); border-radius: 5px;
    display: flex; align-items: center; justify-content: center;
    font-size: 14.5px; white-space: nowrap;
  }
  .address-box strong { font-weight: 600; margin-right: 4px; }
  .phone-row {
    position: absolute; top: 183px; left: 0; width: 100%; height: 23px;
    display: flex; justify-content: center; align-items: center; font-size: 13.5px;
  }
  .phone-row .item { padding: 0 22px; }
  .phone-row .item strong { font-weight: 600; }
  .phone-row .divider { width: 1px; height: 23px; background: var(--rule-grey); }
  .footer-bar { position: absolute; left: 58px; top: 995px; width: 643px; height: 7px; background: var(--navy); }
  .footer-line { position: absolute; left: 58px; top: 1006px; width: 643px; height: 1.5px; background: var(--navy); }
  .footer-title {
    position: absolute; left: 58px; top: 1012px;
    font-family: "Oranienbaum", serif; font-size: 26px; color: var(--navy);
  }
  .page-number {
    position: absolute; right: 67px; top: 1017px;
    font-family: "Oranienbaum", serif; font-size: 18px; color: var(--navy);
  }
</style>
</head>
<body>
  <div class="letterhead">
    <svg class="header-swoosh" viewBox="0 0 759 240" aria-hidden="true">
      <path d="M0,152 C0,200 30,229 65,229 L759,229 L759,219 L65,219 C28,219 0,195 0,152 Z" fill="var(--swoosh-grey)"/>
    </svg>

    <div class="brand">
      <div class="brand-square"></div>
      <div class="brand-name">
        <span class="firm">CORBIN ALVEY</span>
        <span class="practice-row"><span class="rule"></span><span class="practice">LAW</span><span class="rule"></span></span>
      </div>
    </div>

    <div class="website">www.calveylegal.example</div>

    <div class="address-box">
      <strong>Law Office of Corbin Alvey, PLLC,</strong> 615 Marlowe St. Ste #300-214, Houston, TX 77002
    </div>

    <div class="phone-row">
      <span class="item"><strong>Office:</strong> 832.555.0143</span>
      <span class="divider"></span>
      <span class="item"><strong>Direct:</strong> 713.555.0186</span>
      <span class="divider"></span>
      <span class="item"><strong>Fax:</strong> 832.555.0127</span>
    </div>

    <div class="footer-bar"></div>
    <div class="footer-line"></div>
    <div class="footer-title">Letter of Protection</div>
    <div class="page-number">Page 1</div>
  </div>
</body>
</html>
```